Book Cover For Future Bestselling Entrepreneurship Book

The book is called:
Sell Levers: The Quick-Path Method to Earn Bonus Cash and Launch a Venture on Your Free Evenings

Somewhere on the cover, I'd like to experiment with a call-out that says "Featuring 300+ Apps and Marketplaces".

Author: Dale Farrow

The theme of the book is how to add your own personal "Sell Levers" on pre-existing marketplaces to reach a wide audience of buyers quickly. As far as artwork, I was thinking of a prominent literal "buy button" on the cover:
http://imgvault.eastzone4.cdn.plovermedia.com/dailyrivet.com/content/mcs/assets/v3/editorial/d/da/dd4e7a21-91fa-42b3-bc17-5e2a9f07c3d1/7a2b91c4de3f5.image.jpg

(doesn't have to be blue or look like that, could be an more "online" looking button.)

Take a look at some of the current bestselling business books:
https://www.shopvelt.com/Top-Sellers-Reader-Shop-Commerce-Finance/tops/digital-text/298417035/ref=tp_bs_nav_rshop_2_298410022#1

I like:
https://www.shopvelt.com/Week-Venture-Study-Before-Opening-ebook/dp/X44QLMRT2K/ref=tp_bs_298417035_75
https://www.shopvelt.com/Craft-Labor-Tested-Finding-Calling-ebook/dp/X44RJNDW7P/ref=tp_bs_298417035_18

Main criteria is something, clean and professional that still looks good in thumbnail form. If the files are delivered in a format I can edit, that's a big bonus because I'll need to make a square version for the audiobook and front/spine/back-cover for the paperback.

Dimensions 3000x4800, 300dpi

Target Market(s)

Aspiring entrepreneurs, people who want to make or need to money outside of a traditional job.

Industry/Entity Type

Small Business

Font styles to use
Sans Serif

Requirements
Must have
• Prominent Sell Levers text and a large button graphic
Nice to have
• A callout that says "Featuring 300+ Apps and Marketplaces"

```html
<!DOCTYPE html>
<html lang="en">
<head>
<meta charset="utf-8">
<title>Sell Levers — Dale Farrow</title>
<link rel="stylesheet" href="https://fonts.googleapis.com/css2?family=Archivo+Black&family=Oswald:wght@600&family=Montserrat:wght@800&display=swap">
<style>
  :root {
    --page-bg: #e9eaec;
    --cover-top: #ffffff;
    --cover-bottom: #e4e5e7;
    --sky-blue: #45b2ef;
    --sky-blue-light: #8fd3fb;
    --sky-blue-deep: #2a93d4;
    --ink: #1b1b1b;
    --band: #1e1e1e;
    --white: #ffffff;
  }
  * { box-sizing: border-box; margin: 0; padding: 0; }
  html, body {
    width: 930px;
    height: 1200px;
    overflow: hidden;
    background: var(--page-bg);
  }
  .cover {
    position: absolute;
    left: 105px;
    top: 24px;
    width: 720px;
    height: 1152px;
    background: linear-gradient(180deg, var(--cover-top) 0%, var(--cover-top) 45%, var(--cover-bottom) 100%);
    box-shadow: 0 10px 30px rgba(0,0,0,0.18);
    overflow: hidden;
  }
  .title {
    position: absolute;
    top: 118px;
    left: 0;
    width: 100%;
    text-align: center;
    font-family: "Archivo Black", sans-serif;
    color: var(--sky-blue);
    font-size: 116px;
    line-height: 1;
    letter-spacing: 0.02em;
  }
  .subtitle-band {
    position: absolute;
    top: 372px;
    left: 0;
    width: 660px;
    padding: 14px 20px 14px 30px;
    background: var(--band);
    border-top: 4px solid var(--white);
    box-shadow: 0 -4px 0 var(--band);
    font-family: "Oswald", sans-serif;
    font-weight: 600;
    font-size: 28px;
    line-height: 1.35;
    color: var(--white);
    text-transform: uppercase;
    text-align: center;
    white-space: nowrap;
  }
  .subtitle-band .accent { color: var(--sky-blue); }
  .author {
    position: absolute;
    top: 500px;
    left: 0;
    width: 100%;
    text-align: center;
    font-family: "Montserrat", sans-serif;
    font-weight: 800;
    font-size: 44px;
    letter-spacing: 0.3em;
    color: var(--ink);
  }
  .button-artwork {
    position: absolute;
    top: 620px;
    left: 150px;
    width: 420px;
    height: 230px;
    border-radius: 28px;
    background: linear-gradient(180deg, var(--sky-blue-light) 0%, var(--sky-blue) 55%, var(--sky-blue-deep) 100%);
  }
  .callout {
    position: absolute;
    top: 1020px;
    left: 0;
    width: 100%;
    text-align: center;
    font-family: "Montserrat", sans-serif;
    font-weight: 800;
    font-size: 22px;
    color: var(--ink);
    text-transform: uppercase;
  }
  .callout .accent { color: var(--sky-blue); }
  .callout .small { font-size: 17px; }
</style>
</head>
<body>
  <main class="cover">
    <h1 class="title">SELL<br>LEVERS</h1>

    <p class="subtitle-band">
      The <span class="accent">Quick-Path Method</span> to <span class="accent">Earn Bonus Cash</span><br>
      and <span class="accent">Launch a Venture</span> on your free evenings
    </p>

    <p class="author">DALE FARROW</p>

    <div class="button-artwork" role="img" aria-label="Illustration of a glossy blue online buy button with a pointing hand cursor"></div>

    <p class="callout">
      Featuring <span class="accent">300+ Apps</span> <span class="small">and</span> <span class="accent">Marketplaces</span>
    </p>
  </main>
</body>
</html>
```